2019 Ignite a Hidden Titan Within (Cardio Calendar)

I would like to put together a calendar of cardio workouts for the year. I would have 4 different workouts per week + 2 basic steady state workouts. I envision a picture of me on the top page and along with the challenge of the month description and the 3 different types of cardio description. on the bottom page would be the calendar for that month with the workout typed into the box. I am not sure if a boxed calendar would be enough space to write each workout in so I am open to more ideas on how to present the workouts

Target Market(s)

Women 20-60 years old
moms
couples
men
athletes

Industry/Entity Type

Fitness

Font styles to use
Sans Serif

Colors

Designer to choose colors to be used in the design.

Requirements
Must have
• Ability to incorporate 4 different workouts per week in a downloadable calendar style
• I want to have a different picture available for each month
• modern, bold, but simple and clean presentation
Nice to have
• picture at the top, with a description of the 3 different types of workouts for that month.
• On the bottom would be space for separate days of each workout
Should not have
• NA

```html
<!DOCTYPE html>
<html lang="en">
<head>
<meta charset="utf-8">
<title>January 2019 – Ignite a Hidden Titan Within Cardio Calendar</title>
<link rel="stylesheet" href="https://fonts.googleapis.com/css2?family=Oswald:wght@500;600;700&family=Roboto+Condensed:wght@400&display=swap">
<style>
  :root {
    --navy: #1b2638;
    --red: #e3203e;
    --deep-red: #8e1020;
    --blush: #f5d0c4;
    --mist: #c6c8ce;
    --faded: #8a909c;
    --paper: #ffffff;
    --backdrop: #e8e9ec;
    --turf: #2f6a1e;
  }
  * { box-sizing: border-box; margin: 0; padding: 0; }
  html, body { width: 1200px; height: 800px; overflow: hidden; }
  body { background: var(--backdrop); font-family: "Oswald", sans-serif; }

  .calendar-page {
    position: absolute; left: 342px; top: 0;
    width: 516px; height: 800px;
    background: var(--paper);
    box-shadow: 0 0 18px rgba(0,0,0,.12);
    overflow: hidden;
  }

  .hero-photo {
    position: absolute; left: 0; top: 0; width: 516px; height: 240px;
    background:
      radial-gradient(ellipse 60% 70% at 55% 40%, #3b3f46 0%, #15171b 70%),
      #0f1013;
    overflow: hidden;
  }
  .hero-photo::after {
    content: ""; position: absolute; left: 0; right: 0; bottom: 0; height: 70px;
    background: linear-gradient(180deg, rgba(47,106,30,0) 0%, var(--turf) 70%, #24561a 100%);
  }
  .hero-month {
    position: absolute; left: -14px; top: -22px;
    font-size: 96px; font-weight: 700; line-height: 1;
    color: var(--deep-red); opacity: .55; letter-spacing: 1px;
    z-index: 1;
  }
  .hero-year {
    position: absolute; right: -6px; bottom: -26px;
    font-size: 104px; font-weight: 700; line-height: 1;
    color: #b5142a; opacity: .8;
    z-index: 1;
  }

  .month-heading {
    position: absolute; left: 18px; top: 248px; width: 482px; height: 50px;
  }
  .month-name {
    position: absolute; left: 0; top: 0;
    font-size: 40px; font-weight: 700; color: var(--red); line-height: 1.15;
  }
  .month-rule {
    position: absolute; left: 144px; right: 70px; top: 37px;
    height: 3px; background: var(--navy);
  }
  .month-year {
    position: absolute; right: 0; top: 14px;
    font-size: 24px; font-weight: 700; color: var(--red); line-height: 1.1;
  }

  .weekday-row {
    position: absolute; left: 6px; top: 308px;
    display: flex;
  }
  .weekday {
    width: 72px; text-align: center;
    font-size: 15px; font-weight: 600; color: var(--navy);
  }
  .weekday.is-sunday { color: var(--red); }

  .month-grid { position: absolute; left: 0; top: 333px; width: 516px; height: 370px; }

  .cell-body { fill: var(--paper); stroke: var(--navy); stroke-width: 1; }
  .cell-body.sunday { fill: var(--blush); }
  .cell-body.saturday { fill: var(--mist); }
  .cell-cap { fill: var(--navy); }
  .day-num { font-family: "Oswald", sans-serif; font-weight: 600; font-size: 22px; fill: #fff; text-anchor: middle; }
  .day-num.sunday { fill: var(--red); }
  .day-num.outside { fill: var(--faded); }
  .workout { font-family: "Roboto Condensed", sans-serif; font-size: 7px; fill: var(--navy); }
  .workout .reps { fill: var(--red); }

  .notes-row { position: absolute; left: 6px; top: 718px; display: flex; gap: 8px; }
  .note-box { width: 162px; height: 72px; background: var(--navy); }
</style>
</head>
<body>
<main class="calendar-page">
  <section class="hero-photo" role="img" aria-label="Photo of an athlete stretching on a foam roller on a floodlit turf field">
    <span class="hero-month">JANUARY</span>
    <span class="hero-year">2019</span>
  </section>

  <header class="month-heading">
    <h1 class="month-name">JANUARY</h1>
    <span class="month-rule"></span>
    <span class="month-year">2019</span>
  </header>

  <div class="weekday-row">
    <span class="weekday is-sunday">SUN</span>
    <span class="weekday">MON</span>
    <span class="weekday">TUE</span>
    <span class="weekday">WED</span>
    <span class="weekday">THU</span>
    <span class="weekday">FRI</span>
    <span class="weekday">SAT</span>
  </div>

  <svg class="month-grid" viewBox="0 0 516 370" xmlns="http://www.w3.org/2000/svg">
    <defs>
      <polygon id="hex" points="35,0 70,14 70,60 35,74 0,60 0,14"/>
      <polygon id="hex-cap" points="35,0 70,14 70,36 0,36 0,14"/>
      <g id="w1"><text class="workout" x="10" y="44"><tspan class="reps">2</tspan> Lorem Ipsum</text></g>
      <g id="w2"><use href="#w1"/><text class="workout" x="10" y="51.5"><tspan class="reps">2</tspan> Lorem Ipsum</text></g>
      <g id="w3"><use href="#w2"/><text class="workout" x="10" y="59"><tspan class="reps">2</tspan> Lorem Ipsum</text></g>
      <g id="w4"><use href="#w3"/><text class="workout" x="10" y="66.5"><tspan class="reps">2</tspan> Lorem Ipsum</text></g>
    </defs>

    <!-- week 1 -->
    <g transform="translate(6,0)"><use href="#hex" class="cell-body sunday"/><use href="#hex-cap" class="cell-cap"/><text class="day-num outside" x="35" y="28">30</text></g>
    <g transform="translate(78,0)"><use href="#hex" class="cell-body"/><use href="#hex-cap" class="cell-cap"/><text class="day-num outside" x="35" y="28">31</text></g>
    <g transform="translate(150,0)"><use href="#hex" class="cell-body"/><use href="#hex-cap" class="cell-cap"/><text class="day-num" x="35" y="28">1</text><use href="#w3"/></g>
    <g transform="translate(222,0)"><use href="#hex" class="cell-body"/><use href="#hex-cap" class="cell-cap"/><text class="day-num" x="35" y="28">2</text><use href="#w2"/></g>
    <g transform="translate(294,0)"><use href="#hex" class="cell-body"/><use href="#hex-cap" class="cell-cap"/><text class="day-num" x="35" y="28">3</text><use href="#w4"/></g>
    <g transform="translate(366,0)"><use href="#hex" class="cell-body"/><use href="#hex-cap" class="cell-cap"/><text class="day-num" x="35" y="28">4</text><use href="#w4"/></g>
    <g transform="translate(438,0)"><use href="#hex" class="cell-body saturday"/><use href="#hex-cap" class="cell-cap"/><text class="day-num" x="35" y="28">5</text><use href="#w4"/></g>

    <!-- week 2 -->
    <g transform="translate(6,73)"><use href="#hex" class="cell-body sunday"/><use href="#hex-cap" class="cell-cap"/><text class="day-num sunday" x="35" y="28">6</text></g>
    <g transform="translate(78,73)"><use href="#hex" class="cell-body"/><use href="#hex-cap" class="cell-cap"/><text class="day-num" x="35" y="28">7</text><use href="#w2"/></g>
    <g transform="translate(150,73)"><use href="#hex" class="cell-body"/><use href="#hex-cap" class="cell-cap"/><text class="day-num" x="35" y="28">8</text><use href="#w1"/></g>
    <g transform="translate(222,73)"><use href="#hex" class="cell-body"/><use href="#hex-cap" class="cell-cap"/><text class="day-num" x="35" y="28">9</text><use href="#w2"/></g>
    <g transform="translate(294,73)"><use href="#hex" class="cell-body"/><use href="#hex-cap" class="cell-cap"/><text class="day-num" x="35" y="28">10</text><use href="#w3"/></g>
    <g transform="translate(366,73)"><use href="#hex" class="cell-body"/><use href="#hex-cap" class="cell-cap"/><text class="day-num" x="35" y="28">11</text><use href="#w4"/></g>
    <g transform="translate(438,73)"><use href="#hex" class="cell-body saturday"/><use href="#hex-cap" class="cell-cap"/><text class="day-num" x="35" y="28">12</text><use href="#w4"/></g>

    <!-- week 3 -->
    <g transform="translate(6,146)"><use href="#hex" class="cell-body sunday"/><use href="#hex-cap" class="cell-cap"/><text class="day-num sunday" x="35" y="28">13</text></g>
    <g transform="translate(78,146)"><use href="#hex" class="cell-body"/><use href="#hex-cap" class="cell-cap"/><text class="day-num" x="35" y="28">14</text><use href="#w1"/></g>
    <g transform="translate(150,146)"><use href="#hex" class="cell-body"/><use href="#hex-cap" class="cell-cap"/><text class="day-num" x="35" y="28">15</text><use href="#w3"/></g>
    <g transform="translate(222,146)"><use href="#hex" class="cell-body"/><use href="#hex-cap" class="cell-cap"/><text class="day-num" x="35" y="28">16</text><use href="#w1"/></g>
    <g transform="translate(294,146)"><use href="#hex" class="cell-body"/><use href="#hex-cap" class="cell-cap"/><text class="day-num" x="35" y="28">17</text><use href="#w4"/></g>
    <g transform="translate(366,146)"><use href="#hex" class="cell-body"/><use href="#hex-cap" class="cell-cap"/><text class="day-num" x="35" y="28">18</text><use href="#w2"/></g>
    <g transform="translate(438,146)"><use href="#hex" class="cell-body saturday"/><use href="#hex-cap" class="cell-cap"/><text class="day-num" x="35" y="28">19</text><use href="#w3"/></g>

    <!-- week 4 -->
    <g transform="translate(6,219)"><use href="#hex" class="cell-body sunday"/><use href="#hex-cap" class="cell-cap"/><text class="day-num sunday" x="35" y="28">20</text></g>
    <g transform="translate(78,219)"><use href="#hex" class="cell-body"/><use href="#hex-cap" class="cell-cap"/><text class="day-num" x="35" y="28">21</text><use href="#w3"/></g>
    <g transform="translate(150,219)"><use href="#hex" class="cell-body"/><use href="#hex-cap" class="cell-cap"/><text class="day-num" x="35" y="28">22</text><use href="#w2"/></g>
    <g transform="translate(222,219)"><use href="#hex" class="cell-body"/><use href="#hex-cap" class="cell-cap"/><text class="day-num" x="35" y="28">23</text><use href="#w2"/></g>
    <g transform="translate(294,219)"><use href="#hex" class="cell-body"/><use href="#hex-cap" class="cell-cap"/><text class="day-num" x="35" y="28">24</text><use href="#w1"/></g>
    <g transform="translate(366,219)"><use href="#hex" class="cell-body"/><use href="#hex-cap" class="cell-cap"/><text class="day-num" x="35" y="28">25</text><use href="#w4"/></g>
    <g transform="translate(438,219)"><use href="#hex" class="cell-body saturday"/><use href="#hex-cap" class="cell-cap"/><text class="day-num" x="35" y="28">26</text><use href="#w2"/></g>

    <!-- week 5 -->
    <g transform="translate(6,292)"><use href="#hex" class="cell-body sunday"/><use href="#hex-cap" class="cell-cap"/><text class="day-num sunday" x="35" y="28">27</text></g>
    <g transform="translate(78,292)"><use href="#hex" class="cell-body"/><use href="#hex-cap" class="cell-cap"/><text class="day-num" x="35" y="28">28</text><use href="#w1"/></g>
    <g transform="translate(150,292)"><use href="#hex" class="cell-body"/><use href="#hex-cap" class="cell-cap"/><text class="day-num" x="35" y="28">29</text><use href="#w3"/></g>
    <g transform="translate(222,292)"><use href="#hex" class="cell-body"/><use href="#hex-cap" class="cell-cap"/><text class="day-num" x="35" y="28">30</text><use href="#w3"/></g>
    <g transform="translate(294,292)"><use href="#hex" class="cell-body"/><use href="#hex-cap" class="cell-cap"/><text class="day-num" x="35" y="28">31</text><use href="#w2"/></g>
    <g transform="translate(366,292)"><use href="#hex" class="cell-body"/><use href="#hex-cap" class="cell-cap"/><text class="day-num outside" x="35" y="28">1</text></g>
    <g transform="translate(438,292)"><use href="#hex" class="cell-body saturday"/><use href="#hex-cap" class="cell-cap"/><text class="day-num outside" x="35" y="28">2</text></g>
  </svg>

  <footer class="notes-row">
    <div class="note-box"></div>
    <div class="note-box"></div>
    <div class="note-box"></div>
  </footer>
</main>
</body>
</html>
```